Printing company needs website!

A printing company would like a new professional website (made with wix). Now they don't have a website, but they want a unique, beautiful, clear site. Of course they provide the content themselves, we are now looking for the beautiful design with some mockups. You can see several of their projects on their instagram & facebook.
Www.pagenook.com/velmoor and https://www.snapfolio.com/velmoor.be/ logos are attached.

```html
<!DOCTYPE html>
<html lang="en">
<head>
<meta charset="utf-8">
<title>Velmoor – Printing Services</title>
<link href="https://fonts.googleapis.com/css2?family=Poppins:wght@300;400;500;600;700;800&display=swap" rel="stylesheet">
<style>
:root{
  --teal:#3fbfa5;
  --teal-dark:#2aa79b;
  --cyan:#19b3d4;
  --yellow:#f6c20c;
  --yellow-light:#fbd713;
  --ink:#1d2a33;
  --grey:#6f7780;
  --footer:#0f2f3b;
  --grid:#eef3f6;
}
*{margin:0;padding:0;box-sizing:border-box}
html,body{width:1200px;height:4027px;overflow:hidden}
body{font-family:'Poppins',sans-serif;color:var(--ink);background:#fff;position:relative}
.abs{position:absolute}
.brand{display:flex;align-items:center;gap:10px;font-weight:700;color:var(--ink);font-size:32px}
.brand-dot{width:26px;height:26px;border-radius:50%;background:var(--teal)}
.brand-tag{font-size:9px;color:var(--teal);font-weight:400;letter-spacing:.5px}

/* header */
.site-header{top:0;left:0;width:1200px;height:81px}
.nav{top:30px;left:366px;display:flex;font-size:15px}
.nav a{color:var(--ink);text-decoration:none;position:absolute;white-space:nowrap}
.nav a.active{color:var(--teal)}
.nav a.active::after{content:"";position:absolute;left:0;right:0;top:28px;height:2px;background:var(--teal)}
.phone-btn{left:953px;top:23px;width:166px;height:36px;border-radius:18px;background:var(--teal);color:#fff;font-size:14px;font-weight:600;display:flex;align-items:center;justify-content:center;gap:8px}

/* hero */
.hero{top:81px;left:0;width:1200px;height:622px;overflow:hidden}
.hero-photo{position:absolute;left:0;top:0;width:1200px;height:622px;border-radius:560px 0 0 560px/640px 0 0 640px;
  background:linear-gradient(100deg,#1fb5c9 0%,#2bb7a8 28%,#5d7c86 48%,#a34a6f 62%,#4a3b48 78%,#2a2a2e 100%)}
.hero-welcome{left:116px;top:202px;color:#fff;font-size:27px;font-weight:400}
.hero-title{left:114px;top:240px;color:#fff;font-size:62px;font-weight:800;line-height:64px}
.btn-yellow{background:var(--yellow);color:#fff;font-weight:600;font-size:14px;border-radius:24px;display:flex;align-items:center;justify-content:center;letter-spacing:.3px}
.hero-dots{left:560px;top:587px;display:flex;gap:10px}
.hero-dots span{width:11px;height:11px;border-radius:50%;background:#fff}
.hero-dots span.on{background:var(--yellow)}

/* services */
.grid-bg{background-color:#fff;background-image:linear-gradient(var(--grid) 1px,transparent 1px),linear-gradient(90deg,var(--grid) 1px,transparent 1px);background-size:22px 22px}
.services{top:703px;left:0;width:1200px;height:628px}
.eyebrow{font-size:22px;color:var(--teal);font-weight:400}
.heading{font-size:42px;font-weight:400;color:var(--ink)}
.heading b{font-weight:700}
.kicker-line{left:127px;top:866px;width:3px;height:62px;background:var(--teal)}
.body-text{font-size:15px;line-height:26px;color:var(--grey)}
.btn-outline{border:2px solid var(--teal);color:var(--teal);border-radius:26px;font-size:14px;font-weight:600;display:flex;align-items:center;justify-content:center}
.card{background:#fff;border-radius:8px;box-shadow:0 6px 22px rgba(0,0,0,.06);padding:26px 22px}
.card h3{font-size:17px;font-weight:600;color:var(--teal);margin:14px 0 6px}
.card p{font-size:11px;line-height:17px;color:var(--grey)}
.card.featured{background:var(--teal);border-bottom:5px solid var(--yellow)}
.card.featured h3,.card.featured p{color:#fff}

/* about */
.about{top:1331px;left:0;width:1200px;height:553px;background:linear-gradient(90deg,var(--yellow-light),var(--yellow))}
.about-ring{left:114px;top:1389px;width:454px;height:454px;border-radius:50%;border:3px solid #fff}
.about-ring2{left:124px;top:1399px;width:434px;height:434px;border-radius:50%;border:1.5px solid #fff}
.about-photo{left:138px;top:1413px;width:406px;height:406px;border-radius:50%;background:radial-gradient(circle at 50% 45%,#8b8e92,#4c5258 70%,#353a40)}
.about .txt{color:#fff}
.btn-teal{background:var(--teal);color:#fff;border-radius:24px;font-weight:600;font-size:14px;display:flex;align-items:center;justify-content:center}

/* why */
.feature-icon{width:80px;height:80px;border-radius:50%;border:2px solid var(--teal);display:flex;align-items:center;justify-content:center}
.feature-icon.y{border-color:var(--yellow)}
.feature h4{font-size:16px;font-weight:700;color:var(--ink)}
.feature p{font-size:13px;color:var(--grey)}
.why-frame{left:675px;top:1975px;width:423px;height:358px;border-top:6px solid var(--teal);border-right:6px solid var(--teal)}
.why-photo{left:605px;top:1988px;width:478px;height:404px;background:linear-gradient(135deg,#3a3f46 0%,#6f7d8a 35%,#d7a15a 55%,#3c6fa6 75%,#cfd5da 100%)}

/* gallery */
.gallery{top:2477px;left:0;width:1200px;height:581px}
.gal-card{top:2650px;width:306px;height:311px;border-radius:4px;text-align:center;padding-top:38px;overflow:hidden}
.gal-card h3{font-size:25px;font-weight:700;letter-spacing:.5px}
.gal-card p{font-size:13px;margin-top:2px}
.gal-card .shot{position:absolute;left:40px;right:40px;bottom:0;height:190px;border-radius:4px 4px 0 0}

/* contact */
.contact{top:3058px;left:0;width:1200px;height:567px;background:linear-gradient(90deg,var(--teal) 0%,#2cb6be 55%,var(--cyan) 100%);overflow:hidden}
.field{background:#fff;border:1px solid #d9dfe3;font-size:12px;color:var(--grey);padding:12px 14px}
.contact-ring{left:662px;top:3134px;width:416px;height:416px;border-radius:50%;border:2px solid #fff}
.contact-photo{left:675px;top:3147px;width:390px;height:390px;border-radius:50%;background:radial-gradient(circle at 50% 55%,#e8ecef,#9aa3ab 60%,#5c646c)}

/* footer */
.footer{top:3625px;left:0;width:1200px;height:402px;background:var(--footer);color:#fff}
.f-col h5{font-size:15px;font-weight:600;letter-spacing:.3px}
.f-col ul{list-style:none;margin-top:22px}
.f-col li{font-size:12px;height:27px;color:#dfe7ea}
.f-bar{width:3px;height:24px;background:var(--yellow)}
.f-div{width:1px;height:160px;background:rgba(255,255,255,.15)}
.f-contact{font-size:12px;line-height:15px;color:#dfe7ea}
</style>
</head>
<body>

<header class="abs site-header">
  <div class="abs" style="left:94px;top:22px">
    <div class="brand"><span class="brand-dot"></span>Velmoor</div>
    <div class="brand-tag" style="margin:-4px 0 0 98px">waar alles kan</div>
  </div>
  <nav class="abs nav">
    <a class="active" style="left:0">About Us</a>
    <a style="left:111px">Our Services</a>
    <a style="left:248px">Printing</a>
    <a style="left:351px">Our Work</a>
    <a style="left:465px">Contact Us</a>
  </nav>
  <div class="abs phone-btn">
    <svg width="18" height="18" viewBox="0 0 24 24"><circle cx="12" cy="12" r="11" fill="#fff"/><path d="M8 6.5l2 .2 1 2.6-1.3 1a7 7 0 003.2 3.2l1-1.3 2.6 1 .2 2c-4.5.8-9.3-4-8.7-8.7z" fill="#3fbfa5"/></svg>
    0470 1234 56
  </div>
</header>

<section class="abs hero">
  <div class="hero-photo" role="img" aria-label="Large format printer producing a colourful print, with a teal overlay on the left"></div>
  <p class="abs hero-welcome">Welcome to Velmoor</p>
  <h1 class="abs hero-title">BEST PRINTING<br>SERVICES</h1>
  <div class="abs btn-yellow" style="left:120px;top:381px;width:186px;height:46px">REQUEST QUOTE</div>
  <div class="abs hero-dots"><span></span><span></span><span></span><span class="on"></span></div>
</section>

<section class="abs services grid-bg"></section>
<div class="abs kicker-line"></div>
<p class="abs eyebrow" style="left:144px;top:859px">Who We Are</p>
<h2 class="abs heading" style="left:142px;top:882px"><b>Printing</b> Services</h2>
<p class="abs body-text" style="left:130px;top:953px;width:385px">Lorem ipsum dolor sit amet, consectetur adipiscing elit, sed do eiusmod tempor incididunt ut labore et dolore magna aliqua.</p>
<div class="abs btn-outline" style="left:130px;top:1061px;width:222px;height:50px">VIEW ALL SERVICES</div>

<div class="abs card" style="left:575px;top:777px;width:227px;height:211px">
  <svg width="52" height="50" viewBox="0 0 52 50" fill="none" stroke="#f6c20c" stroke-width="2"><rect x="4" y="4" width="30" height="34" rx="3"/><rect x="18" y="16" width="30" height="26" rx="3"/><circle cx="11" cy="13" r="4"/></svg>
  <h3>Poster Printing</h3>
  <p>Lorem ipsum dolor sit amet, consectetur adipiscing elit, sed do eiusmod tempor inci</p>
</div>
<div class="abs card" style="left:831px;top:805px;width:227px;height:211px">
  <svg width="56" height="48" viewBox="0 0 56 48" fill="none" stroke="#f6c20c" stroke-width="2"><rect x="4" y="14" width="48" height="26" rx="2"/><rect x="14" y="4" width="28" height="10"/><path d="M14 28h28v16H14z"/></svg>
  <h3>Card Printing</h3>
  <p>Lorem ipsum dolor sit amet, consectetur adipiscing elit, sed do eiusmod tempor inci</p>
</div>
<div class="abs card featured" style="left:583px;top:1012px;width:226px;height:216px">
  <svg width="60" height="56" viewBox="0 0 60 56" fill="none" stroke="#fff" stroke-width="2"><path d="M4 14l18-8v44L4 54z"/><path d="M22 6l18 6v40l-18-2z"/><path d="M40 12l16-6v40l-16 6z"/></svg>
  <h3>Brochure Printing</h3>
  <p>Lorem ipsum dolor sit amet, consectetur adipiscing elit, sed do eiusmod tempor inci</p>
</div>
<div class="abs card" style="left:833px;top:1038px;width:226px;height:212px">
  <svg width="54" height="54" viewBox="0 0 54 54" fill="none" stroke="#f6c20c" stroke-width="2"><path d="M27 4l22 12v24L27 50 5 40V16z"/><path d="M5 16l22 12 22-12M27 28v22"/></svg>
  <h3>Product Printing</h3>
  <p>Lorem ipsum dolor sit amet, consectetur adipiscing elit, sed do eiusmod tempor inci</p>
</div>

<section class="abs about"></section>
<div class="abs about-ring"></div>
<div class="abs about-ring2"></div>
<div class="abs about-photo" role="img" aria-label="Two print workers in overalls checking a print in the workshop"></div>
<p class="abs eyebrow txt" style="left:620px;top:1437px;color:#fff">Who We Are</p>
<h2 class="abs heading" style="left:620px;top:1460px;color:#fff;font-size:46px">About <b>Velmoor</b></h2>
<p class="abs body-text" style="left:622px;top:1548px;width:470px;color:#fff;font-size:15px;line-height:24px">Lorem ipsum dolor sit amet, consectetur adipiscing elit, sed do eiusmod tempor incididunt ut labore et dolore</p>
<p class="abs body-text" style="left:622px;top:1608px;width:470px;color:#fff;font-size:15px;line-height:24px">Ut enim ad minim veniam, quis nostrud exercitation ullamco laboris nisi ut aliquip ex ea commodo consequat. Duis aute irure dolor in reprehenderit in voluptate velit esse cillum dolore eu fugiat ab illo inventore veritatis et quasi</p>
<div class="abs btn-teal" style="left:620px;top:1730px;width:177px;height:45px">LEARN MORE</div>

<h2 class="abs heading" style="left:138px;top:2000px;font-size:34px">Why choose <b>Velmoor</b></h2>
<div class="abs feature" style="left:129px;top:2088px;display:flex;gap:22px;align-items:center">
  <div class="feature-icon"><svg width="36" height="40" viewBox="0 0 36 40" fill="none" stroke="#3fbfa5" stroke-width="2"><circle cx="18" cy="15" r="11"/><circle cx="18" cy="15" r="5"/><path d="M11 24l-4 13 6-3 3 5 2-10M25 24l4 13-6-3-3 5"/></svg></div>
  <div><h4>QUALITY PRINTING</h4><p>Lorem ipsum dolor sit amet consectetur</p></div>
</div>
<div class="abs feature" style="left:129px;top:2180px;display:flex;gap:22px;align-items:center">
  <div class="feature-icon y"><svg width="40" height="36" viewBox="0 0 40 36" fill="none" stroke="#f6c20c" stroke-width="2"><rect x="4" y="4" width="32" height="28"/><path d="M4 12h32M14 4v28M26 4v28"/></svg></div>
  <div><h4>FLEXIBLE PRICING</h4><p>Lorem ipsum dolor sit amet consectetur</p></div>
</div>
<div class="abs feature" style="left:129px;top:2277px;display:flex;gap:22px;align-items:center">
  <div class="feature-icon"><svg width="36" height="40" viewBox="0 0 36 40" fill="none" stroke="#3fbfa5" stroke-width="2"><rect x="6" y="4" width="22" height="32" rx="2"/><path d="M11 12h12M11 18h12M11 24h8M30 14l4-2M30 20h4M30 26l4 2"/></svg></div>
  <div><h4>OFFSET PRINTING</h4><p>Lorem ipsum dolor sit amet consectetur</p></div>
</div>
<div class="abs why-frame"></div>
<div class="abs why-photo" role="img" aria-label="Close-up of a wide format printer printing a city skyline"></div>

<section class="abs gallery grid-bg"></section>
<p class="abs eyebrow" style="left:0;width:1200px;top:2514px;text-align:center;font-size:19px">Project Gallery</p>
<h2 class="abs heading" style="left:0;width:1200px;top:2536px;text-align:center;font-size:38px"><b>Our Printing</b> Work</h2>
<div class="abs" style="left:561px;top:2593px;width:78px;height:4px;background:var(--teal)"></div>

<div class="abs gal-card" style="left:133px;background:var(--yellow);color:#fff">
  <h3>STICKERS</h3><p>voor een boodschap die blijft plakken</p>
  <div class="shot" role="img" aria-label="Coffee bags with printed sticker labels" style="background:linear-gradient(90deg,#d8b98a,#c2946a 45%,#2a2522 60%,#1d1a18)"></div>
</div>
<div class="abs gal-card" style="left:453px;background:var(--teal);color:#fff">
  <h3>DOLORE FUGIAT</h3><p>voor een boodschap die blijft plakken</p>
  <div class="shot" role="img" aria-label="Printed property banner showing a modern apartment building" style="top:140px;height:120px;background:linear-gradient(180deg,#d7dde0,#8a969c)"></div>
</div>
<div class="abs gal-card" style="left:770px;background:#fff;color:var(--grey);box-shadow:0 6px 22px rgba(0,0,0,.06)">
  <h3 style="color:var(--teal)">DOLORE FUGIAT</h3><p>voor een boodschap die blijft plakken</p>
  <div class="shot" role="img" aria-label="Hand holding a blue printed shop opening flyer" style="left:70px;right:20px;background:linear-gradient(160deg,#2d4fb0,#1c3a8f 60%,#e6c9b4)"></div>
</div>

<section class="abs contact">
  <div class="abs" style="left:-150px;top:40px;width:620px;height:620px;border-radius:50%;border:60px solid rgba(255,255,255,.06)"></div>
</section>
<p class="abs eyebrow" style="left:139px;top:3160px;color:#fff;font-size:20px">Get in touch</p>
<h2 class="abs heading" style="left:139px;top:3180px;color:#fff;font-size:40px"><b>Contact</b> Us</h2>
<div class="abs" style="left:139px;top:3184px;width:160px"></div>
<div class="abs field" style="left:139px;top:3258px;width:228px;height:41px">First Name</div>
<div class="abs field" style="left:374px;top:3258px;width:229px;height:41px">Last Name</div>
<div class="abs field" style="left:139px;top:3305px;width:228px;height:40px">Phone Number</div>
<div class="abs field" style="left:374px;top:3305px;width:229px;height:40px">Email address</div>
<div class="abs field" style="left:139px;top:3352px;width:464px;height:81px">Message</div>
<div class="abs btn-yellow" style="left:136px;top:3450px;width:173px;height:42px">SEND ENQUIRY</div>
<div class="abs contact-ring"></div>
<div class="abs contact-photo" role="img" aria-label="Printed sheets stacked on a press delivery table"></div>

<footer class="abs footer">
  <div class="abs" style="left:117px;top:88px">
    <div class="brand" style="color:#fff;font-size:36px"><span class="brand-dot"></span>Velmoor</div>
    <div class="brand-tag" style="margin:-4px 0 0 112px">waar alles kan</div>
  </div>
  <p class="abs" style="left:134px;top:155px;width:240px;font-size:12px;line-height:19px;color:#8ea7b0">Lorem ipsum dolor sit amet, consectetur adipiscing elit, sed do eiusmod tempor incididunt ut labore et.</p>

  <div class="abs f-div" style="left:445px;top:60px"></div>
  <div class="abs f-div" style="left:653px;top:60px"></div>
  <div class="abs f-div" style="left:870px;top:60px"></div>

  <div class="abs f-col" style="left:447px;top:64px">
    <div style="display:flex;gap:12px;align-items:center"><span class="f-bar"></span><h5>NAVIGATION</h5></div>
    <ul style="margin-left:15px"><li>About Us</li><li>Printing Services</li><li>Why We Are</li><li>Testimonials</li></ul>
  </div>
  <div class="abs f-col" style="left:653px;top:64px">
    <div style="display:flex;gap:26px;align-items:center"><span class="f-bar"></span><h5>RESOURCES</h5></div>
    <ul style="margin-left:29px"><li>Our Work</li><li>Blogs</li><li>Contact Us</li><li>Privacy Policy</li></ul>
  </div>
  <div class="abs f-col" style="left:870px;top:66px">
    <div style="display:flex;gap:22px;align-items:center"><span class="f-bar"></span><h5>CONTACT US</h5></div>
  </div>
  <div class="abs f-contact" style="left:896px;top:112px;display:flex;gap:14px">
    <svg width="18" height="18" viewBox="0 0 24 24"><path d="M6 3l4 .4 1.6 4.4-2.2 1.6a11 11 0 005.2 5.2l1.6-2.2 4.4 1.6L21 18c-7.6 1.4-16.4-7.4-15-15z" fill="none" stroke="#3fbfa5" stroke-width="2"/></svg>
    <div>Phone<br><span style="font-size:15px;color:#fff">0470 1234 56</span></div>
  </div>
  <div class="abs f-contact" style="left:896px;top:160px;display:flex;gap:14px">
    <svg width="18" height="18" viewBox="0 0 24 24" fill="none" stroke="#3fbfa5" stroke-width="2"><circle cx="12" cy="12" r="9"/><path d="M3 12h18M12 3c3 3 3 15 0 18M12 3c-3 3-3 15 0 18"/></svg>
    <div>Website<br>www.velmoor.be</div>
  </div>
  <div class="abs f-contact" style="left:896px;top:208px;display:flex;gap:14px">
    <svg width="18" height="18" viewBox="0 0 24 24" fill="none" stroke="#3fbfa5" stroke-width="2"><rect x="3" y="5" width="18" height="14"/><path d="M3 5l9 8 9-8"/></svg>
    <div>Email<br>info@velmoor.be</div>
  </div>

  <div class="abs" style="left:0;top:312px;width:1200px;height:1px;background:rgba(255,255,255,.12)"></div>
  <p class="abs" style="left:0;width:1200px;top:340px;text-align:center;font-size:12px;color:#b6c6cc">Copyright © 2022 Velmoor All Right Reserved</p>
</footer>

</body>
</html>
```